Lunaryth needs a elegant mystical business card design

The theme of Lunaryth is centered on Kemetic/Ancient Egyptian Spirituality. My business sells handmade scented candles, mystic oils, body sprays, tarot readings and more. I would like my business card to reflect an elegant and mystical look. Hieroglyphs around the borders would be a cool idea. Also, the main colors I am working with is Black and Gold= colors of royalty. Black background. The business card will be double sided. The back will have the logo, and the front will have the basic information (ie name, title, business, phone, email, website, etc..)

Target Market(s)

The target market are people into metaphysics, holistic healing, ancient Egyptian culture, aromatherapy, occult science, and the esoteric.

Industry/Entity Type

Business

Contact Information for Business Card

Name: Marisol T. Pike
Title: Owner
Business: LUNARYTH
Phone: 555.210.4473
Website: www.Lunaryth.example
Facebook, Instagram, and twitter icons

Font styles to use
Serif
Decorative

Requirements
Must have
• My logo, and website.
Nice to have
• Ancient Egyptian hieroglyphs, Elegant designs around the border, or encircling the logo.

```html
<!DOCTYPE html>
<html lang="en">
<head>
<meta charset="utf-8">
<title>Lunaryth — Business Card</title>
<link rel="stylesheet" href="https://fonts.googleapis.com/css2?family=Cinzel:wght@400;600;700&display=swap">
<style>
  :root {
    --backdrop: #5e4a30;
    --card-black: #0b0b0b;
    --card-black-sheen: #2a2a2a;
    --gold-deep: #8c6a3b;
    --gold-mid: #b8965f;
    --gold-light: #e2cda0;
    --gold-ink: #c8a35c;
    --ink-dark: #1a1309;
  }
  * { margin: 0; padding: 0; box-sizing: border-box; }
  html, body {
    width: 1200px; height: 843px; overflow: hidden;
    background: var(--backdrop);
  }
  .canvas {
    position: relative; width: 1200px; height: 843px;
    background: var(--backdrop);
    font-family: "Cinzel", serif;
  }
  .card {
    position: absolute; width: 580px; height: 331px;
    border-radius: 22px;
    box-shadow: 0 14px 34px rgba(0,0,0,0.45);
  }
  .card-back {
    left: 80px; top: 120px;
    background: linear-gradient(115deg, var(--card-black) 0%, var(--card-black-sheen) 22%, var(--card-black) 40%, var(--card-black) 100%);
    display: flex; align-items: center; justify-content: center;
  }
  .brand-name {
    color: var(--gold-ink);
    font-weight: 600; font-size: 46px; letter-spacing: 6px;
  }
  .card-front {
    left: 540px; top: 392px;
    background: linear-gradient(100deg, var(--gold-deep) 0%, var(--gold-light) 28%, var(--gold-mid) 55%, var(--gold-light) 80%, var(--gold-deep) 100%);
    color: var(--ink-dark);
    text-align: center;
    padding-top: 44px;
  }
  .flourish-top {
    display: block; margin: 0 auto;
    width: 250px; height: 40px;
    border-radius: 20px;
    background: linear-gradient(90deg, transparent, rgba(26,19,9,0.55), transparent);
  }
  .holder-name {
    margin-top: 14px;
    font-weight: 700; font-size: 30px; letter-spacing: 1px;
  }
  .holder-title { font-size: 17px; letter-spacing: 2px; margin-top: 2px; }
  .contact-line { font-size: 17px; margin-top: 10px; letter-spacing: 0.5px; }
  .contact-web { font-size: 17px; margin-top: 2px; letter-spacing: 0.5px; }
  .flourish-bottom {
    display: block; margin: 8px auto 0;
    width: 380px; height: 44px;
    border-radius: 22px;
    background: linear-gradient(90deg, rgba(26,19,9,0.6), rgba(26,19,9,0.15) 50%, rgba(26,19,9,0.6));
  }
</style>
</head>
<body>
  <main class="canvas">
    <section class="card card-back" aria-label="Card back">
      <span class="brand-name">LUNARYTH</span>
    </section>

    <section class="card card-front" aria-label="Card front">
      <span class="flourish-top" role="img" aria-label="Ornamental scroll flourish"></span>
      <h1 class="holder-name">Marisol T. Pike</h1>
      <p class="holder-title">Owner</p>
      <p class="contact-line">P: 555.210.4473 | info@lunaryth.example</p>
      <p class="contact-web">www.Lunaryth.example</p>
      <span class="flourish-bottom" role="img" aria-label="Swash flourish with a row of five small stars"></span>
    </section>
  </main>
</body>
</html>
```